Stationary Design - KM Facial Plastics

We are looking for a stylish and professional stationary design for a facial plastic surgeon. The stationary design will be for letterhead, business card, appointment cards and envelopes.
The design must be slick and aesthetically pleasing whilst incorporating the style of our logo as attached below.

Target Market(s)

Adults of all ages

Font styles to use
Serif
Script

Requirements
Must have
• Must be an aesthetically pleasing, stylish and professional design that includes the required information in a captivating layout.
• Must also be welcoming with a balanced design and a clean crisp finish.
• Details should include:
• Mr Tobias Wrenfield - Consultant Otolaryngologist & Facial Plastic Surgeon
• Phone: 03 5618 2947
• Fax: 03 5619 7084
• Email: info@kmfacialplastics.example.com.au
• Consulting from: Bendigo, Echuca, Epping, Waverley & Melbourne CBD
• Appointment Card should include:
• Date, time, fee and location as per the attached example.
• location addresses are:
• 31 Harlow Street Echuca Vic 3564
• 148 Brennock Street Bendigo Vic 3550
• Level 2, 217 Mabley Street, Epping Vic 3076
• Level 4, 263 Denholm Street Melbourne Vic 3000
Should not have
• Clutter

```html
<!DOCTYPE html>
<html lang="en">
<head>
<meta charset="utf-8">
<title>KM Facial Plastics – Business Card</title>
<link href="https://fonts.googleapis.com/css2?family=Cinzel:wght@400;600&family=Montserrat:wght@400;500&display=swap" rel="stylesheet">
<style>
  :root {
    --backdrop: #8f8f8f;
    --card-dark: #3d3d3f;
    --card-dark-light: #4c4c4e;
    --card-white: #ffffff;
    --band: #4a4a4c;
    --band-facet: #555557;
    --ink: #1e1e1e;
    --ink-soft: #3a3a3a;
    --paper-text: #f2f2f2;
  }
  * { margin: 0; padding: 0; box-sizing: border-box; }
  html, body { width: 1089px; height: 1200px; overflow: hidden; }
  body {
    background: var(--backdrop);
    position: relative;
    font-family: "Montserrat", Arial, sans-serif;
  }
  .card {
    position: absolute;
    left: 84px;
    width: 920px;
    height: 522px;
    box-shadow: 0 6px 18px rgba(0,0,0,0.35);
    overflow: hidden;
  }
  .card--front {
    top: 58px;
    background: radial-gradient(ellipse at 45% 45%, var(--card-dark-light) 0%, var(--card-dark) 70%);
  }
  .card--back {
    top: 620px;
    background: var(--card-white);
  }

  /* practice name */
  .brand-name {
    position: absolute;
    font-family: "Montserrat", Arial, sans-serif;
    font-weight: 400;
    white-space: nowrap;
  }
  .card--front .brand-name {
    left: 0; right: 0;
    top: 222px;
    text-align: center;
    color: var(--paper-text);
    font-size: 40px;
    letter-spacing: 0.02em;
  }
  .card--back .brand-name {
    left: 0; width: 374px;
    top: 250px;
    text-align: center;
    color: var(--ink-soft);
    font-size: 24px;
  }
  .front-email {
    position: absolute;
    left: 0; right: 0;
    bottom: 44px;
    text-align: center;
    color: var(--paper-text);
    font-size: 17px;
    letter-spacing: 0.42em;
  }

  .band {
    position: absolute;
    left: 374px; top: 0;
    width: 64px; height: 522px;
  }
  .contact-icon {
    position: absolute;
    left: 384px;
    width: 44px; height: 44px;
  }
  .practitioner {
    position: absolute;
    left: 457px; top: 118px;
  }
  .practitioner__name {
    font-family: "Cinzel", Georgia, serif;
    font-weight: 400;
    font-size: 38px;
    color: var(--ink);
    letter-spacing: 0.01em;
    white-space: nowrap;
  }
  .practitioner__role {
    margin-top: 12px;
    font-size: 12.5px;
    color: var(--ink-soft);
  }
  .contact-line {
    position: absolute;
    left: 457px;
    font-size: 19px;
    color: var(--ink);
  }
</style>
</head>
<body>

  <section class="card card--front" aria-label="Business card front">
    <p class="brand-name">KM Facial Plastics</p>
    <p class="front-email">ADMIN@HARLOWENTCLINIC.EXAMPLE.COM.AU</p>
  </section>

  <section class="card card--back" aria-label="Business card back">
    <p class="brand-name">KM Facial Plastics</p>

    <svg class="band" viewBox="0 0 64 522" aria-hidden="true">
      <polygon points="0,2 32,18 64,2 64,22 32,38 0,22" fill="var(--band)"/>
      <polygon points="0,34 32,50 64,34 64,522 0,522" fill="var(--band)"/>
      <polygon points="0,330 64,300 64,380 0,410" fill="var(--band-facet)"/>
    </svg>

    <svg class="contact-icon" style="top:100px" viewBox="0 0 44 44" aria-hidden="true">
      <circle cx="22" cy="22" r="19" fill="none" stroke="#fff" stroke-width="2.5"/>
      <circle cx="22" cy="16" r="5.5" fill="#fff"/>
      <path d="M11 33 Q12 23 22 23 Q32 23 33 33 Z" fill="#fff"/>
    </svg>
    <svg class="contact-icon" style="top:255px" viewBox="0 0 44 44" aria-hidden="true">
      <circle cx="22" cy="22" r="19" fill="none" stroke="#fff" stroke-width="2.5"/>
      <path d="M11 22 L22 12 L33 22" fill="none" stroke="#fff" stroke-width="2.5" stroke-linejoin="round"/>
      <path d="M15 21 V31 H20 V25 H24 V31 H29 V21" fill="none" stroke="#fff" stroke-width="2.2"/>
    </svg>
    <svg class="contact-icon" style="top:311px" viewBox="0 0 44 44" aria-hidden="true">
      <circle cx="22" cy="22" r="19" fill="none" stroke="#fff" stroke-width="2.5"/>
      <path d="M16 12 L19 12 L21 17 L18.5 19 Q20 24 25 25.5 L27 23 L32 25 L32 28 Q31 32 27 31 Q15 28 13 17 Q12 13 16 12 Z" fill="#fff"/>
    </svg>
    <svg class="contact-icon" style="top:366px" viewBox="0 0 44 44" aria-hidden="true">
      <circle cx="22" cy="22" r="19" fill="none" stroke="#fff" stroke-width="2.5"/>
      <rect x="12" y="15" width="5" height="16" rx="1" fill="#fff"/>
      <rect x="18.5" y="12" width="13" height="19" rx="1" fill="none" stroke="#fff" stroke-width="2"/>
      <rect x="21" y="15" width="8" height="4" fill="#fff"/>
      <rect x="21" y="22" width="2" height="2" fill="#fff"/>
      <rect x="24.5" y="22" width="2" height="2" fill="#fff"/>
      <rect x="21" y="26" width="2" height="2" fill="#fff"/>
      <rect x="24.5" y="26" width="2" height="2" fill="#fff"/>
    </svg>

    <div class="practitioner">
      <h1 class="practitioner__name">Mr Tobias Wrenfield</h1>
      <p class="practitioner__role">Consultant Otolaryngologist &amp; Facial Plastic Surgeon</p>
    </div>
    <p class="contact-line" style="top:265px">148 Brennock Street Bendigo</p>
    <p class="contact-line" style="top:321px">03 5618 2947</p>
    <p class="contact-line" style="top:376px">03 5619 7084</p>
  </section>

</body>
</html>
```